Recreate a label for a champagne bottle [See attached example]

I'm needing to recreate a label for a champagne bottle label to give as closing gifts to clients when they purchase a home. Please include the following text "Welcome Home", my initials "R.T", "Established Year", the hashtag #BubTORVA and my logo (attached). I prefer to have a black or white background with a crisp, easy to read cursive font similar to the Dunmore bourbon font. I want it to look as similar of a layout to the Valdorca label as possible

Target Market(s)

Luxury

Font styles to use
Decorative
Script

Colors

Designer to choose only greyscale colors for use in the design.

Requirements
Must have
• "Welcome Home", my initials "R.T", "Established Year", the hashtag #BubTORVA and my logo
Nice to have
• Clean cursive font, easy to read, luxury look.
Should not have
• Clutter, too much design.

```html
<!DOCTYPE html>
<html lang="en">
<head>
<meta charset="utf-8">
<title>Welcome Home – Champagne Label</title>
<link href="https://fonts.googleapis.com/css2?family=Pinyon+Script&family=Montserrat:wght@400;500;700&display=swap" rel="stylesheet">
<style>
  :root {
    --page: #000000;
    --label-face: #231f20;
    --silver-dark: #7d7f82;
    --silver-mid: #a9abae;
    --silver-light: #d2d3d5;
    --gold-dark: #9a7420;
    --gold-mid: #c9a640;
    --gold-light: #e6cf78;
    --ink-white: #ffffff;
  }
  html, body {
    margin: 0;
    padding: 0;
    width: 1200px;
    height: 1000px;
    overflow: hidden;
    background: var(--page);
  }
  .canvas {
    position: relative;
    width: 1200px;
    height: 1000px;
    background: var(--page);
  }
  .label {
    position: absolute;
    left: 263px;
    top: 163px;
    width: 672px;
    height: 672px;
    background: linear-gradient(90deg, var(--silver-mid) 0%, var(--silver-light) 45%, var(--silver-mid) 75%, var(--silver-dark) 100%);
  }
  .label-face {
    position: absolute;
    left: 36px;
    top: 36px;
    width: 600px;
    height: 600px;
    background: var(--label-face);
    color: var(--ink-white);
    font-family: "Montserrat", sans-serif;
  }
  .est-row {
    position: absolute;
    top: 88px;
    left: 0;
    width: 100%;
    display: flex;
    justify-content: center;
    align-items: center;
    gap: 22px;
  }
  .est-row .est-text {
    font-size: 12px;
    letter-spacing: 4px;
    font-weight: 400;
  }
  .brand-mark {
    display: flex;
    flex-direction: column;
    align-items: center;
    gap: 6px;
  }
  .brand-mark .brand-square {
    width: 14px;
    height: 14px;
    background: var(--ink-white);
  }
  .brand-mark .brand-name {
    font-size: 17px;
    font-weight: 700;
    letter-spacing: 3px;
    text-transform: uppercase;
  }
  .welcome-script {
    position: absolute;
    left: 0;
    width: 100%;
    text-align: center;
    font-family: "Pinyon Script", cursive;
    font-size: 128px;
    line-height: 1;
    background: linear-gradient(90deg, var(--gold-dark) 0%, var(--gold-light) 40%, var(--gold-mid) 70%, var(--gold-dark) 100%);
    -webkit-background-clip: text;
    background-clip: text;
    color: transparent;
    margin: 0;
  }
  .welcome-script.line-one { top: 172px; }
  .welcome-script.line-two { top: 306px; }
  .initials {
    position: absolute;
    top: 448px;
    left: 0;
    width: 100%;
    text-align: center;
    font-size: 40px;
    font-weight: 700;
    letter-spacing: 2px;
  }
  .hashtag {
    position: absolute;
    top: 533px;
    left: 0;
    width: 100%;
    text-align: center;
    font-size: 23px;
    letter-spacing: 3px;
    text-transform: uppercase;
    font-weight: 500;
  }
  .hashtag strong { font-weight: 700; }
</style>
</head>
<body>
  <div class="canvas">
    <div class="label">
      <div class="label-face">
        <div class="est-row">
          <span class="est-text">ESTD</span>
          <div class="brand-mark">
            <span class="brand-square"></span>
            <span class="brand-name">Lintel</span>
          </div>
          <span class="est-text">2023</span>
        </div>
        <p class="welcome-script line-one">Welcome</p>
        <p class="welcome-script line-two">Home</p>
        <div class="initials">R.T</div>
        <div class="hashtag">#BUB<strong>TORVA</strong></div>
      </div>
    </div>
  </div>
</body>
</html>
```